Relocation/furniture installation company needs new business cards

we are a relocation and furniture installation company mainly dealing with corporate clients and we are looking for new business card ideas. Cards should incorporate our logo and list our website, phone number and services. The company is only 2 years old but with more staff joining we are in the need for more business cards, so something with an awesome design that is eye catching would go a long way to insure we get our name out there and look good to potential new clients.

Target Market(s)

Corporate

Industry/Entity Type

Trade

Contact Information for Business Card

www.mervoline.co.nz
0508 4 bravok

furniture installation
business relocations
joinery installation
commercial property maintenance

Colors
0592cd
34a7d8
85cae6
85acd3
0356a4
cfdfed
cee9f5
757575
474747

Requirements
Must have
• Business relocations and furniture installation specialists
Nice to have
• something that incorporates our logo.

```html
<!DOCTYPE html>
<html lang="en">
<head>
<meta charset="utf-8">
<title>Mervoline Business Card</title>
<link rel="stylesheet" href="https://fonts.googleapis.com/css2?family=Carlito:wght@400;700&display=swap">
<style>
  :root {
    --navy: #2b3a94;
    --cyan: #55c6da;
    --ink: #222428;
    --rule: #4a56a6;
    --card: #ffffff;
    --page: #e9eaec;
    --ghost-light: #f4f5f6;
    --ghost-dark: #e3e5e8;
  }
  * { box-sizing: border-box; margin: 0; padding: 0; }
  html, body {
    width: 1200px;
    height: 1200px;
    overflow: hidden;
    background: var(--page);
    font-family: "Carlito", "Calibri", sans-serif;
  }
  .card {
    position: absolute;
    left: 50px;
    top: 294px;
    width: 1100px;
    height: 612px;
    background: var(--card);
    overflow: hidden;
    box-shadow: 0 6px 24px rgba(0,0,0,0.12);
  }
  .card__backdrop {
    position: absolute;
    left: 300px;
    top: 40px;
    width: 620px;
    height: 500px;
    background: linear-gradient(160deg, var(--ghost-light) 0%, var(--ghost-dark) 55%, var(--ghost-light) 100%);
    opacity: 0.8;
  }
  .brand {
    position: absolute;
    left: 72px;
    top: 150px;
    display: flex;
    align-items: center;
    gap: 18px;
  }
  .brand__mark {
    width: 34px;
    height: 34px;
    background: var(--navy);
  }
  .brand__name {
    font-weight: 700;
    font-size: 78px;
    letter-spacing: 6px;
    color: var(--navy);
    line-height: 1;
  }
  .contact {
    position: absolute;
    left: 72px;
    top: 298px;
    font-size: 30px;
    line-height: 1.3;
    color: var(--ink);
  }
  .contact__label { color: var(--navy); }
  .divider {
    position: absolute;
    left: 72px;
    top: 392px;
    width: 960px;
    height: 2px;
    background: var(--rule);
  }
  .services {
    position: absolute;
    left: 72px;
    top: 414px;
    font-size: 30px;
    line-height: 1.25;
    color: var(--ink);
  }
  .services__title {
    font-weight: 700;
    color: var(--navy);
  }
  .band {
    position: absolute;
    bottom: 0;
    height: 34px;
  }
  .band--navy { left: 0; width: 560px; background: var(--navy); }
  .band--cyan { left: 570px; right: 0; background: var(--cyan); }
</style>
</head>
<body>
  <main class="card">
    <div class="card__backdrop" role="img" aria-label="Faint photograph of a modern office building in soft grey tones"></div>

    <div class="brand">
      <span class="brand__mark"></span>
      <span class="brand__name">MERVOLINE</span>
    </div>

    <div class="contact">
      <p><span class="contact__label">Tel:</span> 0508 4 bravok</p>
      <p><span class="contact__label">Web:</span> www.mervoline.co.nz</p>
    </div>

    <div class="divider"></div>

    <div class="services">
      <p class="services__title">Service</p>
      <p>furniture installation | business relocations</p>
      <p>joinery installation | commercial property maintenance</p>
    </div>

    <div class="band band--navy"></div>
    <div class="band band--cyan"></div>
  </main>
</body>
</html>
```